Business Card Design Project 4 Construction Business

I am after a creative, but sleek and simple/ clean business card design. This design will form the basis of future items and might include a logo or simply a creative way to lay out the text of my company name 'kestrel ventures'
I like the simplicity of black and white however I would also be happy to see a splash of colour introduced somehow to give the text some interest and make it stand out.
I would like a double sided card.
I am young (ish!) and professional, offering construction and project management services, what I don't want is the traditional builders type card featuring a cheesy hammer/ saw image etc.
As the company name, kestrel ventures, suggests, we focus on working closely and collaboratively together, in synergy with all stakeholders involved in the projects that we undertake
Construction

```html
<!DOCTYPE html>
<html lang="en">
<head>
<meta charset="utf-8">
<title>Kestrel Ventures – Business Card</title>
<link rel="stylesheet" href="https://fonts.googleapis.com/css2?family=Michroma&family=Exo+2:ital,wght@0,300;1,300&display=swap">
<style>
  :root {
    --ink: #000000;
    --sand: #a6976e;
    --paper: #ffffff;
    --type-dark: #000000;
  }
  html, body {
    margin: 0;
    padding: 0;
    overflow: hidden;
    background: var(--ink);
  }
  .card {
    position: relative;
    width: 1200px;
    height: 686px;
    overflow: hidden;
    background: var(--ink);
  }
  .card__backdrop {
    position: absolute;
    inset: 0;
    width: 100%;
    height: 100%;
  }
  .card__backdrop .sweep { fill: var(--sand); }
  .line {
    position: absolute;
    margin: 0;
    white-space: nowrap;
    text-align: right;
    line-height: 1;
  }
  .company {
    right: 68px;
    top: 143px;
    font-family: "Michroma", sans-serif;
    font-size: 58px;
    letter-spacing: 3px;
    word-spacing: 10px;
    color: var(--paper);
  }
  .person {
    right: 64px;
    top: 255px;
    font-family: "Exo 2", sans-serif;
    font-weight: 300;
    font-size: 54px;
    color: var(--paper);
  }
  .role {
    right: 65px;
    top: 328px;
    font-family: "Exo 2", sans-serif;
    font-weight: 300;
    font-style: italic;
    font-size: 38px;
    color: var(--paper);
  }
  .contact {
    font-family: "Michroma", sans-serif;
    font-size: 26px;
    letter-spacing: 2px;
    word-spacing: 10px;
    color: var(--type-dark);
  }
  .contact--street { right: 552px; top: 386px; }
  .contact--city   { right: 552px; top: 424px; }
  .contact--email  { right: 360px; top: 486px; letter-spacing: 2px; }
  .contact--web    { right: 360px; top: 520px; letter-spacing: 2px; }
  .contact--phone  { right: 552px; top: 582px; }
</style>
</head>
<body>
  <main class="card">
    <svg class="card__backdrop" viewBox="0 0 1050 600" preserveAspectRatio="none" aria-hidden="true">
      <path class="sweep" d="M0,0 L1050,0 L1050,2 C700,15 262,60 262,150 C262,235 450,300 610,355 C720,392 790,420 785,455 C780,520 400,570 0,598 Z"/>
    </svg>

    <h1 class="line company">Kestrel Ventures</h1>
    <p class="line person">Liam Carrow</p>
    <p class="line role">Director</p>

    <p class="line contact contact--street">12 Tallis Rd.</p>
    <p class="line contact contact--city">Harbourton NSW 2099</p>
    <p class="line contact contact--email">liam@kestrelventuresgroup.com.au</p>
    <p class="line contact contact--web">www.kestrelventuresgroup.com.au</p>
    <p class="line contact contact--phone">ph. 0400 555 018</p>
  </main>
</body>
</html>
```